Civora - a Political Plebescite app.

There is a current app in the App Store (worldwide) and Play Store (worldwide) called yourTally (with an owl logo). The UX needs to be redesigned to make it more visually pleasing.

The requirement is to build a UX that is suitable for both iOS and Android - i.e. consistent look for both platforms. The design is to span the variety of sizes available from smart devices - phones and tablets. The layout as it stands is portrait only, and a secondary design to encompass landscape is wanted.

You would need to download the app to get a feel for all the functionality - there are 3 visible forms (currently) and a hidden form, that will be used in the near future - this hidden form will look similar to the main (first) form.

To get full functionality you need to do the following:
Go to the Options page
Toggle the top slide
Click on UNREGISTERED
Select a state/territory

I know this is a bit non-intuitive - in the "real" product these steps are automated - but for this release the user gets to choose.

Once this is done - the other button(s) appear in the top left of the screen - and data is available to be displayed.

The current forms are included in this brief. The Options screen will ultimately not be showing all the current data, only the lower slider (or other indicator) and the associated version and copyright notices. The hidden screen is much like the main screen - showing the name of the bill and information pertaining to that bill - there needs to be a button (or action site) to toggle between the main and this hidden screen.

Target Market(s)

All eligable voters (currently in Australia)

Industry/Entity Type

Political

Requirements
Should not have
• Do not present to me my own/existing design with the only change being colours and label layout.

```html
<!DOCTYPE html>
<html lang="en">
<head>
<meta charset="utf-8">
<title>Civora – General</title>
<link href="https://fonts.googleapis.com/css2?family=Roboto:wght@300;400&display=swap" rel="stylesheet">
<style>
  :root {
    --header-bg: #d2d5d8;
    --status-text: #ffffff;
    --ink: #474747;
    --ink-soft: #555555;
    --accent: #56648a;
    --accent-dark: #455374;
    --region-green: #3e8a6a;
    --region-red: #a32a1d;
    --live-green: #0a8a18;
    --page-light: #ffffff;
    --page-edge: #d9dadc;
  }
  * { box-sizing: border-box; margin: 0; padding: 0; }
  html, body { width: 674px; height: 1200px; overflow: hidden; }
  body {
    position: relative;
    font-family: "Roboto", sans-serif;
    color: var(--ink);
    background: radial-gradient(ellipse at 50% 42%, var(--page-light) 0%, #f3f3f4 45%, var(--page-edge) 100%);
  }
  .app-header {
    position: absolute; left: 0; top: 0; width: 674px; height: 158px;
    background: var(--header-bg);
  }
  .status-bar {
    position: absolute; left: 0; top: 0; width: 100%; height: 46px;
    color: var(--status-text); font-size: 23px; font-weight: 300;
  }
  .status-bar .carrier { position: absolute; left: 13px; top: 8px; letter-spacing: 0.5px; }
  .status-bar .clock { position: absolute; left: 0; width: 100%; text-align: center; top: 6px; }
  .status-bar .battery { position: absolute; right: 12px; top: 8px; display: flex; align-items: center; gap: 10px; }
  .battery-cell { width: 50px; height: 22px; border: 2px solid var(--status-text); border-radius: 4px; padding: 2px; position: relative; }
  .battery-cell::before { content: ""; display: block; width: 100%; height: 100%; background: var(--status-text); border-radius: 1px; }
  .region-switch { position: absolute; top: 73px; left: 236px; display: flex; align-items: center; gap: 10px; }
  .region {
    width: 42px; height: 34px; display: flex; align-items: center; justify-content: center;
  }
  .region.active { width: 52px; height: 52px; border-radius: 50%; background: #fff; }
  .region span { display: block; width: 34px; height: 26px; border-radius: 7px 12px 6px 10px; }
  .region.green span { background: var(--region-green); }
  .region.red span { background: var(--region-red); }
  .tabs {
    position: absolute; left: 151px; top: 208px; width: 373px; height: 46px;
    display: flex; border: 1px solid var(--accent); border-radius: 23px; overflow: hidden;
  }
  .tab {
    flex: 1; display: flex; align-items: center; justify-content: center;
    font-size: 18px; color: var(--ink-soft); letter-spacing: 0.3px;
  }
  .tab + .tab { border-left: 1px solid var(--accent); }
  .tab.active { background: var(--accent); color: #fff; }
  .content { position: absolute; left: 32px; top: 306px; width: 620px; }
  .content h1 { font-size: 21px; font-weight: 400; line-height: 30px; color: var(--ink); margin-bottom: 22px; }
  .content p { font-size: 16.2px; line-height: 26.2px; font-weight: 400; color: var(--ink-soft); margin-bottom: 26px; hyphens: auto; }
  .chamber { position: absolute; left: 25px; top: 1066px; display: flex; align-items: center; gap: 21px; font-size: 19px; color: #222; }
  .chamber .dot { width: 17px; height: 17px; border-radius: 50%; background: var(--live-green); }
  .pager { position: absolute; right: 22px; top: 1074px; font-size: 21px; color: #222; }
  .tab-bar { position: absolute; left: 0; top: 1118px; width: 674px; height: 82px; display: flex; }
  .tab-bar .action { flex: 1; display: flex; align-items: center; justify-content: center; }
  .tab-bar .settings { background: var(--accent-dark); }
  .tab-bar .help { background: var(--accent); border-left: 1px solid #6d7ba0; }
</style>
</head>
<body>
  <header class="app-header">
    <div class="status-bar">
      <span class="carrier">●●●○○ BELL</span>
      <span class="clock">4:21 PM</span>
      <span class="battery">100% <span class="battery-cell"></span></span>
    </div>
    <nav class="region-switch">
      <div class="region green active" role="img" aria-label="State map: selected state"><span></span></div>
      <div class="region red" role="img" aria-label="State map"><span></span></div>
      <div class="region green" role="img" aria-label="National map"><span></span></div>
      <div class="region red" role="img" aria-label="National map"><span></span></div>
    </nav>
  </header>

  <div class="tabs">
    <div class="tab active">GENERAL</div>
    <div class="tab">FAQ</div>
    <div class="tab">CONTACT</div>
  </div>

  <main class="content">
    <h1>Lorem ipsum dolor sit amet, consectetur adipiscing elit.</h1>
    <p>Nam condimentum leo sed nisi malesuada, sed accumsan metus ultricies. Donec eleifend nibh in ultrices tempus. Morbi id tempor lorem. Suspendisse potenti. Fusce at augue pulvinar, ultricies nisl id, bibendum est. Cras semper ac nulla ut vulputate. Nam faucibus sagittis odio, quis molestie elit sollicitu&shy;din et. Nam dapibus fringilla orci, quis efficitur leo consectetur eu. Vivamus dui lectus, mollis a condimentum consequat, ullamcorper porta lectus. Vi&shy;vamus sit amet justo enim. Donec nec lorem mi. Lorem ipsum dolor sit amet, consectetur adipiscing elit.</p>
    <p>Nam condimentum leo sed nisi malesuada, sed accumsan metus ultricies. Donec eleifend nibh in ultrices tempus. Morbi id tempor lorem. Suspendisse potenti. Fusce at augue pulvinar, ultricies nisl id, bibendum est. Cras semper ac nulla ut vulputate. Nam faucibus sagittis odio, quis molestie elit sollicitu&shy;din et. Nam dapibus fringilla orci, quis efficitur leo consectetur eu. Vivamus dui lectus, mollis a condimentum consequat, ullamcorper porta lectus. Vi&shy;vamus sit amet justo enim. Donec nec lorem mi. Lorem ipsum dolor sit amet, consectetur adipiscing elit.</p>
    <p>Nam condimentum leo sed nisi malesuada, sed accumsan metus ultricies. Donec eleifend nibh in ultrices tempus. Morbi id tempor lorem. Suspendisse potenti. Fusce at augue pulvinar, ultricies nisl id, bibendum est. Cras semper ac nulla ut vulputate. Nam faucibus sagittis odio, quis molestie elit sollicitu&shy;din et. Nam dapibus fringilla orci, quis efficitur leo consectetur eu. Vivamus dui lectus, mollis a condimentum consequat, ullamcorper porta lectus.</p>
  </main>

  <div class="chamber"><span class="dot"></span>Legislative Council</div>
  <div class="pager">1 / 77</div>

  <footer class="tab-bar">
    <div class="action settings">
      <svg width="44" height="44" viewBox="0 0 24 24" aria-label="Settings">
        <path fill="#fff" d="M19.4 13a7.5 7.5 0 0 0 0-2l2.1-1.6-2-3.5-2.5 1a7.6 7.6 0 0 0-1.7-1L15 3.2h-4l-.4 2.7a7.6 7.6 0 0 0-1.7 1l-2.5-1-2 3.5L6.6 11a7.5 7.5 0 0 0 0 2l-2.1 1.6 2 3.5 2.5-1a7.6 7.6 0 0 0 1.7 1l.4 2.7h4l.4-2.7a7.6 7.6 0 0 0 1.7-1l2.5 1 2-3.5zM13 15.3a3.3 3.3 0 1 1 0-6.6 3.3 3.3 0 0 1 0 6.6z" transform="translate(-1 0)"/>
      </svg>
    </div>
    <div class="action help">
      <svg width="44" height="44" viewBox="0 0 44 44" aria-label="Help">
        <circle cx="22" cy="22" r="21" fill="#fff"/>
        <path d="M15.5 17a6.5 6.5 0 1 1 9.6 5.7c-2 1.1-3.1 2.1-3.1 4.3v1" fill="none" stroke="var(--accent)" stroke-width="4" stroke-linecap="round"/>
        <circle cx="22" cy="34" r="2.4" fill="var(--accent)"/>
      </svg>
    </div>
  </footer>
</body>
</html>
```